VORN - Business cards

Business card to be created for Commercial sales staff

Target Market(s)

Commercial businesses

Industry/Entity Type

Commercial

Contact Information for Business Card

Look professional. For commercial clients

Colors
ffffff

Requirements
Must have
• - Vorn Logo
• - Commercial sales staff as postion
• - room for commerical sales manager role
• - person name and their mobile number
• - Website : vornelectrical.com.au
Nice to have
• White background.
• On back of business card just have the logo no other information
Should not have
• Should only have white background on front of card.

```html
<!DOCTYPE html>
<html lang="en">
<head>
<meta charset="utf-8">
<title>VORN – Business cards</title>
<link rel="stylesheet" href="https://fonts.googleapis.com/css2?family=Montserrat:wght@300;400;600;700&display=swap">
<style>
  :root {
    --page-bg: #b9bdbe;
    --card-bg: #f4f3f0;
    --brand-red: #c4161c;
    --ink: #1d1d1f;
    --ink-soft: #4a4a4c;
    --rule: #b8b8b8;
    --edge: #8c0f14;
  }
  * { box-sizing: border-box; margin: 0; padding: 0; }
  html, body {
    width: 1200px;
    height: 824px;
    overflow: hidden;
    background: var(--page-bg);
    font-family: "Montserrat", sans-serif;
  }
  .canvas {
    width: 1200px;
    height: 824px;
    display: flex;
    align-items: center;
    justify-content: center;
    gap: 48px;
  }
  .card {
    position: relative;
    width: 530px;
    height: 324px;
    background: var(--card-bg);
    border-bottom: 4px solid var(--edge);
    box-shadow: 0 10px 24px rgba(0,0,0,0.18);
  }

  /* Front */
  .card-front .identity {
    position: absolute;
    top: 44px;
    left: 42px;
    display: flex;
    align-items: flex-start;
  }
  .brand-mini {
    display: flex;
    align-items: center;
    gap: 6px;
    padding-top: 6px;
    padding-right: 16px;
  }
  .brand-mini .mark { width: 14px; height: 14px; border-radius: 50%; background: var(--brand-red); }
  .brand-mini .wordmark {
    font-weight: 700;
    font-size: 18px;
    letter-spacing: 1px;
    color: var(--ink);
  }
  .divider {
    width: 1px;
    height: 62px;
    background: var(--rule);
    margin-right: 14px;
  }
  .person .name {
    font-weight: 600;
    font-size: 17px;
    letter-spacing: 1px;
    color: var(--brand-red);
    text-transform: uppercase;
    line-height: 1.25;
  }
  .person .role {
    font-weight: 300;
    font-size: 13.5px;
    color: var(--ink-soft);
    line-height: 1.35;
  }
  .contact {
    position: absolute;
    right: 40px;
    bottom: 34px;
    text-align: right;
    font-weight: 300;
    font-size: 13.5px;
    line-height: 1.5;
    color: var(--ink);
    list-style: none;
  }
  .contact .label { color: var(--brand-red); }

  /* Back */
  .card-back {
    display: flex;
    align-items: center;
    justify-content: center;
  }
  .brand-large {
    display: flex;
    align-items: center;
    gap: 18px;
  }
  .brand-large .mark { width: 40px; height: 40px; border-radius: 50%; background: var(--brand-red); }
  .brand-large .wordmark {
    font-weight: 700;
    font-size: 78px;
    letter-spacing: 3px;
    color: var(--ink);
  }
</style>
</head>
<body>
<main class="canvas">
  <section class="card card-front" aria-label="Business card front">
    <div class="identity">
      <div class="brand-mini">
        <span class="mark"></span>
        <span class="wordmark">VORN</span>
      </div>
      <span class="divider"></span>
      <div class="person">
        <p class="name">Ben Carter</p>
        <p class="role">Manager</p>
        <p class="role">Commerical Sales</p>
      </div>
    </div>
    <ul class="contact">
      <li>Ben@vornelectrical.com.au</li>
      <li><span class="label">(P)</span> 612 555 0184</li>
      <li><span class="label">(C)</span> 415 555 0297</li>
      <li>www.vornelectrical.com.au</li>
    </ul>
  </section>

  <section class="card card-back" aria-label="Business card back">
    <div class="brand-large">
      <span class="mark"></span>
      <span class="wordmark">VORN</span>
    </div>
  </section>
</main>
</body>
</html>
```